Website design: Mobile Physiotherapy, Massage & Personal Training Business

I need a website that reflects a staff of health and fitness professionals. I would like the theme of the website to match the company logo (Harbor Motion Wellness).
This is a link for a competitors website that I am fond of:
http://www.tandrilcare.example.au/
I am open to any and all creative and innovative designs.

Industry/Entity Type

Fitness

```html
<!DOCTYPE html>
<html lang="en">
<head>
<meta charset="utf-8">
<title>Harbor Motion Wellness</title>
<link rel="stylesheet" href="https://fonts.googleapis.com/css2?family=PT+Sans:wght@400;700&family=Noto+Serif:ital,wght@1,700&display=swap">
<style>
:root{
  --red:#c4121a;
  --red-dark:#8e0a0f;
  --ink:#333;
  --text:#444;
  --dark:#111;
  --footer:#3a3a3a;
  --plaque:#ececec;
  --white:#fff;
}
*{margin:0;padding:0;box-sizing:border-box}
html,body{width:875px;height:1200px;overflow:hidden;background:var(--white)}
body{position:relative;font-family:"PT Sans",sans-serif;color:var(--text)}
.abs{position:absolute}

.header{left:0;top:0;width:875px;height:112px;background:radial-gradient(ellipse at 40% 30%,#2d2a26,#0c0b0a 70%)}
.plaque{left:128px;top:0;width:184px;height:64px}
.plaque-name{left:128px;top:24px;width:184px;text-align:center;font-weight:700;font-size:15px;color:var(--red)}
.social-tab{left:584px;top:0;width:128px;height:22px}
.social{left:602px;top:5px;display:flex;gap:14px}
.social span{width:12px;height:12px;border-radius:50%;background:#1c7fc4}
.social span:last-child{background:#e8641b}
.hours-tab{left:468px;top:58px;width:256px;height:23px}
.hours{left:488px;top:64px;font-size:8.5px;color:#333;white-space:nowrap}
.hours a{color:var(--red);text-decoration:none}

.nav{left:126px;top:81px;width:602px;height:31px;background:linear-gradient(#d3141c,#8a0a0f);display:flex;align-items:center}
.nav a{color:var(--white);font-size:8.5px;font-weight:700;text-decoration:none;height:31px;line-height:31px}
.nav .active{background:linear-gradient(#777,#3a3a3a);width:69px;margin-left:8px;text-align:center}
.nav a+a{margin-left:32px}

.hero{left:0;top:112px;width:875px;height:358px;background:radial-gradient(ellipse at 30% 75%,#8a3517 0%,#3b1a10 35%,#16120f 70%)}
.hero-photo{left:476px;top:128px;width:232px;height:342px;background:linear-gradient(160deg,#2a8fd0 0%,#1d5d8c 45%,#3a3a3a 100%);border-radius:110px 110px 0 0;opacity:.85}
.hero-title{left:136px;top:198px;font-family:"Noto Serif",serif;font-style:italic;font-weight:700;font-size:42px;color:var(--white);line-height:1}
.hero-sub{left:136px;top:242px;font-family:"Noto Serif",serif;font-style:italic;font-weight:700;font-size:30px;color:var(--red);line-height:1}
.hero-copy{left:136px;top:275px;width:300px;font-size:8.5px;font-weight:700;color:var(--white);line-height:1.25}

.section-title{font-size:26px;color:var(--ink);font-weight:400;letter-spacing:.3px;line-height:1}
.rule{left:146px;width:560px;height:2px;background:var(--red)}

.card-photo{top:537px;width:171px;height:100px;border:1px solid #ccc}
.card-title{top:654px;font-size:14px;color:var(--ink)}
.card-sub{top:672px;font-size:9px;color:var(--red)}
.card-copy{top:685px;width:175px;font-size:7px;line-height:1.3}
.btn{top:737px;width:56px;height:18px;background:linear-gradient(var(--red),var(--red-dark));color:var(--white);font-size:7px;font-weight:700;text-align:center;line-height:18px}

.date{top:846px;width:39px;height:45px;background:#2b2b2b;color:var(--white);text-align:center;font-size:8px;line-height:1.35;padding-top:3px}
.date b{display:block;font-size:13px;line-height:1.1}
.news-copy{top:846px;width:135px;font-size:7px;line-height:1.3}

.member-name{top:986px;font-size:8.5px;color:var(--red)}
.member-photo{top:1000px;width:78px;height:48px;border:1px solid #ddd}
.member-copy{top:1001px;width:82px;font-size:7px;line-height:1.3}

.footer{left:0;top:1084px;width:875px;height:116px;background:var(--footer)}
.foot-plaque{left:160px;top:1122px;width:108px;height:34px}
.foot-name{left:160px;top:1134px;width:108px;text-align:center;font-weight:700;font-size:8.5px;color:var(--red)}
.foot-legal{left:170px;top:1160px;font-family:"Noto Serif",serif;font-style:italic;font-weight:700;font-size:9px;color:var(--white)}
.foot-links{left:486px;top:1129px;font-size:8.5px;font-weight:700;color:var(--white)}
.foot-phone{left:489px;top:1149px;font-size:8.5px;font-weight:700;color:var(--white)}
</style>
</head>
<body>

<header class="abs header"></header>
<svg class="abs plaque" viewBox="0 0 184 64"><polygon points="14,8 170,8 184,36 170,64 14,64 0,36" fill="var(--plaque)"/></svg>
<div class="abs plaque-name">Harbor Motion Wellness</div>

<svg class="abs social-tab" viewBox="0 0 128 22"><polygon points="0,0 128,0 120,22 8,22" fill="var(--white)"/></svg>
<div class="abs social"><span></span><span></span><span></span><span></span></div>

<svg class="abs hours-tab" viewBox="0 0 256 23"><polygon points="10,0 246,0 256,23 0,23" fill="var(--white)"/></svg>
<div class="abs hours">Mon-Fri: 7.30am-7pm, Sat: 8am-2pm &nbsp;|<a href="#">Register</a>| &nbsp;<a href="#">Login</a></div>

<nav class="abs nav">
  <a class="active" href="#">HOME</a>
  <a href="#">ABOUT US</a>
  <a href="#">SERVICES</a>
  <a href="#">PRODUCTS</a>
  <a href="#">CONTACTS</a>
</nav>

<section class="abs hero"></section>
<div class="abs hero-photo" role="img" aria-label="Woman in a blue running top jogging"></div>
<h1 class="abs hero-title">CHANGE YOUR</h1>
<div class="abs hero-sub">LIFE FOREVER</div>
<p class="abs hero-copy">Lorem ipsum dolor sit amet, consectetur adipiscing elit. Nulddg dfla eu mi varius, scelerisque sapien ac, tempodfr leo. Aenean eget pretium neque.t, consectetur adipiscing elit. Nulla eu mi varius, scelerisque sapien ac, tem-podfr leo. Aenean egling</p>

<h2 class="abs section-title" style="left:146px;top:494px">OUR SERVICES</h2>

<div class="abs card-photo" style="left:146px;background:linear-gradient(135deg,#6b6f78,#c9b9a8)" role="img" aria-label="Therapist stretching a client's leg in a clinic"></div>
<div class="abs card-photo" style="left:340px;background:linear-gradient(135deg,#e9e6e2,#b8a898)" role="img" aria-label="Group doing a yoga stretch"></div>
<div class="abs card-photo" style="left:535px;background:linear-gradient(135deg,#f6f4f0,#e2d2b8)" role="img" aria-label="Woman raising her arms in celebration"></div>

<h3 class="abs card-title" style="left:147px">KEEPING YOU ON TRACK</h3>
<h3 class="abs card-title" style="left:338px">SPECIAL PROGRAM</h3>
<h3 class="abs card-title" style="left:535px">WEIGHT LOSS PROGRAM</h3>
<div class="abs card-sub" style="left:147px">Morbi nibh lectus, ornare non porta</div>
<div class="abs card-sub" style="left:338px">Morbi nibh lectus, ornare non porta</div>
<div class="abs card-sub" style="left:535px">Morbi nibh lectus, ornare non porta</div>
<p class="abs card-copy" style="left:147px">Lorem ipsum dolor sit amet, consectetur adipiscing elit. Curabitur sodales a orci id pulvinar. Dsddffonec porta libero sem, quis faucibus erat ullamcorpefg r sodales.Curabitur sodales a orci id pulvinar.</p>
<p class="abs card-copy" style="left:338px">Lorem ipsum dolor sit amet, consectetur adipiscing elit. Curabitur sodales a orci id pulvinar. Dsddffonec porta libero sem, quis faucibus erat ullamcorpefg r sodales.Curabitur sodales a orci id pulvinar.</p>
<p class="abs card-copy" style="left:535px">Lorem ipsum dolor sit amet, consectetur adipiscing elit. Curabitur sodales a orci id pulvinar. Dsddffonec porta libero sem, quis faucibus erat ullamcorpefg r sodales.Curabitur sodales a orci id pulvinar.</p>
<div class="abs btn" style="left:147px">Read More</div>
<div class="abs btn" style="left:338px">Read More</div>
<div class="abs btn" style="left:535px">Read More</div>

<div class="abs rule" style="top:774px"></div>

<h2 class="abs section-title" style="left:147px;top:802px">RECENT NEWS</h2>
<div class="abs date" style="left:145px"><b>23</b>Sep<br>2014</div>
<div class="abs date" style="left:341px"><b>23</b>Sep<br>2014</div>
<div class="abs date" style="left:537px"><b>23</b>Sep<br>2014</div>
<p class="abs news-copy" style="left:189px">Lorem ipsum dolor sit amet, consecte-tur adipiscing elit. Curabitur sodal essa orci id pulvinar. Dsddffonec porta lopt libero sem, quis faucibus erat ullamcor-pefg r sodales.</p>
<p class="abs news-copy" style="left:385px">Lorem ipsum dolor sit amet, consecte-tur adipiscing elit. Curabitur sodal essa orci id pulvinar. Dsddffonec porta lopt libero sem, quis faucibus erat ullamcor-pefg r sodales.</p>
<p class="abs news-copy" style="left:581px">Lorem ipsum dolor sit amet, consecte-tur adipiscing elit. Curabitur sodal essa orci id pulvinar. Dsddffonec porta lopt libero sem, quis faucibus erat ullamcor-pefg r sodales.</p>

<div class="abs rule" style="top:921px"></div>

<h2 class="abs section-title" style="left:148px;top:946px">ABOUT OUR TEAM</h2>
<div class="abs member-name" style="left:151px">Morbi nibh lectus, ornare</div>
<div class="abs member-name" style="left:350px">Morbi nibh lectus, ornare</div>
<div class="abs member-name" style="left:549px">Morbi nibh lectus, ornare</div>
<div class="abs member-photo" style="left:151px;background:linear-gradient(135deg,#f2f2f2,#6aa6d6)" role="img" aria-label="Portrait of a senior team member"></div>
<div class="abs member-photo" style="left:350px;background:linear-gradient(135deg,#5a7a55,#b4443a)" role="img" aria-label="Portrait of a team member"></div>
<div class="abs member-photo" style="left:549px;background:linear-gradient(135deg,#f4f4f4,#d8b8a0)" role="img" aria-label="Portrait of a young team member"></div>
<p class="abs member-copy" style="left:235px">Lorem ipsum dolor sit amet, consec dfgrtetur adipi scsing elit. Curabi-tur sodalef essa orci id pulvinar.</p>
<p class="abs member-copy" style="left:434px">Lorem ipsum dolor sit amet, consec dfgrtetur adipi scsing elit. Curabi-tur sodalef essa orci id pulvinar.</p>
<p class="abs member-copy" style="left:633px">Lorem ipsum dolor sit amet, consec dfgrtetur adipi scsing elit. Curabi-tur sodalef essa orci id pulvinar.</p>

<footer class="abs footer"></footer>
<div class="abs rule" style="top:1081px"></div>
<svg class="abs foot-plaque" viewBox="0 0 108 34"><polygon points="8,2 100,2 108,17 100,32 8,32 0,17" fill="var(--plaque)"/></svg>
<div class="abs foot-name">Harbor Motion Wellness</div>
<div class="abs foot-legal">2014 © Privacy Policy</div>
<div class="abs foot-links">HOME | ABOUT US | SERVICES | PRODUCTS | CONTACTS</div>
<div class="abs foot-phone">Get In Touch With Us :1 800 555 01 234</div>

</body>
</html>
```